Folder & Business Card for Automation Company
Brightwell Torque Mfr.
Folder & Business Card for Automation Company - Manufacturing
Creative Brief
Professional
Darren Okafor
Vice President
4817 Halvern Road Merriam, KS 66209
do@brightwelltorquemfr.example
www.brightwelltorquemfr.example
Along with a business card we are looking for a design for the front cover of a folder to be used for sales literature. The cover should also include our logo.

```html
<!DOCTYPE html>
<html lang="en">
<head>
<meta charset="utf-8">
<title>Brightwell Torque Mfr. – Folder Cover</title>
<link rel="stylesheet" href="https://fonts.googleapis.com/css2?family=Cinzel:wght@400;700&display=swap">
<style>
  :root {
    --backdrop: #ece7df;
    --paper: #ffffff;
    --fold: #d9d9d9;
    --brand-red: #d71920;
    --band-dark: #262626;
    --band-light: #4a4a4a;
    --ink: #1f1f1f;
    --band-text: #e6e6e6;
  }
  html, body {
    margin: 0;
    padding: 0;
    width: 1200px;
    height: 862px;
    overflow: hidden;
    background: var(--backdrop);
  }
  .folder {
    position: absolute;
    left: 43px;
    top: 43px;
    width: 1114px;
    height: 778px;
    background: var(--paper);
    box-shadow: 0 2px 8px rgba(0,0,0,0.18);
    overflow: hidden;
  }
  .folder-waves {
    position: absolute;
    inset: 0;
    width: 100%;
    height: 100%;
  }
  .fold-line {
    position: absolute;
    left: 557px;
    top: 0;
    width: 1px;
    height: 100%;
    background: var(--fold);
  }
  .brand {
    position: absolute;
    left: 557px;
    width: 557px;
    top: 326px;
    display: flex;
    justify-content: center;
    align-items: center;
    gap: 14px;
    font-family: "Cinzel", serif;
    font-weight: 700;
    font-size: 34px;
    line-height: 38px;
    letter-spacing: 1px;
    color: var(--ink);
  }
  .brand-dot {
    width: 24px;
    height: 24px;
    border-radius: 50%;
    background: var(--brand-red);
    flex: none;
  }
  .brand-name {
    display: flex;
    flex-direction: column;
    white-space: nowrap;
  }
  .contact {
    position: absolute;
    left: 0;
    width: 557px;
    top: 692px;
    text-align: center;
    font-family: "Cinzel", serif;
    font-size: 12px;
    line-height: 19px;
    letter-spacing: 0.5px;
    color: var(--band-text);
  }
  .tagline {
    position: absolute;
    left: 557px;
    width: 557px;
    top: 690px;
    text-align: center;
    font-family: "Cinzel", serif;
    font-size: 17px;
    line-height: 28px;
    letter-spacing: 3px;
    color: var(--band-text);
  }
</style>
</head>
<body>
  <main class="folder">
    <svg class="folder-waves" viewBox="0 0 1114 778" preserveAspectRatio="none" aria-hidden="true">
      <defs>
        <radialGradient id="bandShade" cx="0.5" cy="0.6" r="0.7">
          <stop offset="0" stop-color="var(--band-light)"/>
          <stop offset="1" stop-color="var(--band-dark)"/>
        </radialGradient>
      </defs>
      <path class="swoosh" d="M0 572 C 120 600, 260 640, 420 612 C 520 594, 600 588, 700 592 C 860 598, 1000 570, 1114 566 L 1114 610 C 1000 612, 860 632, 700 630 C 580 628, 480 640, 380 650 C 240 660, 110 640, 0 612 Z" fill="var(--brand-red)"/>
      <path class="band" d="M0 620 C 120 650, 250 680, 390 662 C 480 650, 560 640, 660 642 C 820 646, 980 620, 1114 615 L 1114 778 L 0 778 Z" fill="url(#bandShade)"/>
    </svg>
    <div class="fold-line"></div>

    <div class="brand">
      <span class="brand-dot"></span>
      <span class="brand-name">
        <span>Brightwell</span>
        <span>Torque Mfr.</span>
      </span>
    </div>

    <div class="contact">
      <div class="contact-web">www.brightwelltorquemfr.example</div>
      <div class="contact-phone">913-555-0187</div>
    </div>

    <div class="tagline">
      <div>System Integration</div>
      <div>Since 1977</div>
    </div>
  </main>
</body>
</html>
```